Melodex Icon design for single song release

Design an icon for melodex (eventually, we will need to use the same style to design the 4 side CD cover) for a new song to be released. Needs to follow certain specs: I am attaching a design that I created, but looking for the design to be spiced up a bit. I am happy with the design, font, and style.. Just want to see something a bit more creative.
Specs:
1. An Melodex ICON for my latest single that i need to get released. Here are the specs..
• Finalized design for icon for Melodex: (DLT Logo attached and JPEG dimensions below)
o Name of the song is “WHEN”
Melodex: Your cover art must be:
o 1400 x 1400 pixels
o JPG file type
o 72 - 300dpi (300dpi is the best)
o Less than 25mb
o RGB color scheme (not CMYK)

I have my music logo and the picture, so I have to have something that fits these dimensions for Melodex.

Please do not change the photo. and please keep the photo in color. The song has an edge to it, but don't want over the top.

Target Market(s)

Contemporary Christian; Christian Rock - music has an edge.

Font styles to use
Other font styles liked:
• see example design

Requirements
Must have
• Marla Penwick
• Song title "When"
• Photo
• Dimensions listed above when design if final.
• Photo attached
• Logo attached
• *Please use a color photo; please use the lettering like the example; and the font colors

```html
<!DOCTYPE html>
<html lang="en">
<head>
<meta charset="utf-8">
<title>Marla Penwick – When</title>
<link href="https://fonts.googleapis.com/css2?family=Monoton&family=Josefin+Sans:wght@200;300;400&display=swap" rel="stylesheet">
<style>
  :root {
    --ink: #000000;
    --cream: #f6e6d6;
    --rose: #e8717c;
    --badge-fill: #2b2a2c;
    --badge-edge: #6b3fa3;
    --photo-light: #e6cfa6;
    --photo-mid: #c79a7f;
    --photo-dark: #1a1414;
  }
  html, body {
    margin: 0;
    padding: 0;
    width: 1200px;
    height: 1200px;
    overflow: hidden;
    background: var(--ink);
  }
  .cover {
    position: relative;
    width: 1200px;
    height: 1200px;
    background: var(--ink);
    overflow: hidden;
  }
  .portrait {
    position: absolute;
    left: 201px;
    top: 0;
    width: 800px;
    height: 1200px;
    background:
      radial-gradient(ellipse 48% 42% at 55% 42%, var(--photo-mid) 0%, rgba(199,154,127,0.6) 55%, rgba(199,154,127,0) 80%),
      linear-gradient(180deg, var(--photo-light) 0%, #d9b98e 45%, #7d6350 72%, var(--photo-dark) 88%, var(--ink) 100%);
  }
  .title-block {
    position: absolute;
    left: 686px;
    top: 986px;
    width: 314px;
    height: 214px;
    background: var(--ink);
  }
  .artist-name {
    position: absolute;
    left: 0;
    top: 0;
    width: 200px;
    height: 1200px;
  }
  .artist-name text {
    font-family: "Monoton", sans-serif;
    font-size: 128px;
  }
  .artist-first { fill: var(--cream); }
  .artist-last { fill: var(--rose); }
  .song-title {
    position: absolute;
    left: 0;
    top: 0;
    width: 1200px;
    height: 1200px;
    pointer-events: none;
  }
  .song-title text {
    font-family: "Josefin Sans", sans-serif;
    font-weight: 300;
    font-size: 238px;
    fill: var(--cream);
  }
  .label-badge {
    position: absolute;
    left: 1029px;
    top: 24px;
    width: 143px;
    height: 143px;
    box-sizing: border-box;
    border: 4px solid var(--badge-edge);
    background: var(--badge-fill);
    display: flex;
    align-items: center;
    justify-content: center;
    font-family: "Josefin Sans", sans-serif;
    font-weight: 400;
    font-size: 44px;
    letter-spacing: 2px;
    color: var(--cream);
  }
</style>
</head>
<body>
  <main class="cover">
    <div class="portrait" role="img" aria-label="Colour portrait photo of the artist with long blonde hair, hoop earring and black top"></div>
    <div class="title-block"></div>

    <svg class="artist-name" viewBox="0 0 200 1200" aria-label="Marla Penwick">
      <text transform="translate(150 1086) rotate(-90)" textLength="990" lengthAdjust="spacingAndGlyphs"><tspan class="artist-first">MARLA </tspan><tspan class="artist-last">PENWICK</tspan></text>
    </svg>

    <svg class="song-title" viewBox="0 0 1200 1200" aria-label="When">
      <text x="706" y="1174" textLength="448" lengthAdjust="spacingAndGlyphs">WHEN</text>
    </svg>

    <div class="label-badge">DLT</div>
  </main>
</body>
</html>
```